Yarnful Hours planner/ book cover

YARNFUL HOURS" - A UNIQUE NOTEBOOK FOR CRAFTS. The main goal of a "Yarnful Hours" notebook is to arrange your crafts notes like knitting planner. Its pages are systematically structured, so they are easy to review, and all the information about the started project is in one place. The notebook has a click opening system, so you can remove, insert, change pages.
This is the old design in Latvian language. I want a new, classic, modern cover design for selling book in USA.I prefer original picture rather than download. Maybe for some of yourself drawings. Illustrated color-wash and minimalistic style better than photography.
Look at the pages inside design so that the lid fits. Maybe i want to change some clipart on the inside as well (just small one, like ball of yarn, sweater, can be seen in the picture, more classic style, not so childish, but that's latter), leave yoga clipart and the colors. Check please video.
https://www.vidhollow.example/watch?v=Qm4tLr8wZ2k
www.yarnfulhours.example its my style.

book title- yarnful hours
slogan- its time for sitting to do some knitting
size- 18 x 23,5 x 4 cm

Colors
d3a5cc
eea4c8
fdf2f7
fbd4d5
fdf0f6
ffffff
e34297
a64599
b868aa

```html
<!DOCTYPE html>
<html lang="en">
<head>
<meta charset="utf-8">
<title>Yarnful Hours – Notebook Cover</title>
<link rel="stylesheet" href="https://fonts.googleapis.com/css2?family=Arvo:wght@700&family=Sofia&display=swap">
<style>
  :root {
    --page: #ffffff;
    --cover-pink: #eca4c8;
    --panel-light: #fdf0f6;
    --panel-blush: #fbd4d5;
    --title-pink: #eaa0c6;
    --dot-white: #ffffff;
    --slogan: #fdf2f7;
    --band-stitch: #fdf0f6;
  }
  * { margin: 0; padding: 0; box-sizing: border-box; }
  html, body {
    width: 1079px;
    height: 1200px;
    overflow: hidden;
    background: var(--page);
  }
  .canvas {
    position: relative;
    width: 1079px;
    height: 1200px;
  }
  .cover {
    position: absolute;
    left: 191px;
    top: 155px;
    width: 682px;
    height: 893px;
    background: var(--cover-pink);
  }
  .title-frame {
    position: absolute;
    left: 133px;
    top: 142px;
    width: 416px;
    height: 453px;
  }
  .title-frame svg { position: absolute; inset: 0; }
  .knit-panel {
    position: absolute;
    left: 14px;
    top: 10px;
    width: 387px;
    height: 435px;
    background: linear-gradient(180deg, var(--panel-light), var(--panel-blush) 140%);
    border: 2px solid var(--dot-white);
  }
  .book-title {
    position: absolute;
    left: 14px;
    top: 10px;
    width: 387px;
    height: 435px;
    display: flex;
    flex-direction: column;
    align-items: center;
    justify-content: center;
    gap: 12px;
    font-family: "Arvo", "Rockwell", serif;
    font-weight: 700;
    font-size: 62px;
    line-height: 1;
    letter-spacing: 1px;
    color: var(--title-pink);
    text-align: center;
  }
  .stitch-band {
    position: absolute;
    left: 0;
    width: 694px;
    height: 21px;
    background: var(--band-stitch);
    opacity: 0.85;
  }
  .stitch-band--top { top: 646px; }
  .stitch-band--bottom { top: 816px; }
  .slogan {
    position: absolute;
    left: 0;
    top: 685px;
    width: 682px;
    text-align: center;
    font-family: "Sofia", "Segoe Script", cursive;
    font-size: 47px;
    line-height: 63px;
    color: var(--slogan);
  }
</style>
</head>
<body>
  <div class="canvas">
    <section class="cover">
      <div class="title-frame">
        <svg width="416" height="453" viewBox="0 0 416 453" aria-hidden="true">
          <rect x="4" y="4" width="408" height="445" fill="none" stroke="var(--dot-white)"
                stroke-width="7" stroke-linecap="round" stroke-dasharray="0 21"/>
        </svg>
        <div class="knit-panel" role="img" aria-label="Light pink knitted stitch texture"></div>
        <svg width="416" height="453" viewBox="0 0 416 453" aria-hidden="true">
          <rect x="14" y="10" width="387" height="435" fill="none" stroke="var(--dot-white)"
                stroke-width="9" stroke-linecap="round" stroke-dasharray="0 27"/>
        </svg>
        <h1 class="book-title">
          <span>YARNFUL</span>
          <span>HOURS</span>
        </h1>
      </div>

      <div class="stitch-band stitch-band--top" role="img" aria-label="Row of knitted stitches"></div>
      <p class="slogan">its time for sitting<br>to do some knitting</p>
      <div class="stitch-band stitch-band--bottom" role="img" aria-label="Row of knitted stitches"></div>
    </section>
  </div>
</body>
</html>
```